business card deign

Logo needs the following on it.
1. attached logo
2. Tagline - "From the cooler to the dance floor...we bring the fun!"
3. Name- Delia Fenwick, Founder and CPO
4. Address - 418 E. Harlow Avenue, Ste 2204, Tampa, FL. 33719
5. Phone - 720.555.0187

```html
<!DOCTYPE html>
<html lang="en">
<head>
<meta charset="UTF-8">
<title>Hopwell Business Card</title>
<link href="https://fonts.googleapis.com/css2?family=Poppins:wght@300;400;600;700&display=swap" rel="stylesheet">
<style>
  :root {
    --ink: #111111;
    --paper: #fbfbfb;
    --backdrop: #e6e4e1;
    --mute: #2a2a2a;
  }
  * { margin: 0; padding: 0; box-sizing: border-box; }
  html, body { width: 1200px; height: 900px; overflow: hidden; }
  body {
    background: var(--backdrop);
    font-family: "Poppins", sans-serif;
    color: var(--ink);
    position: relative;
  }
  .card {
    position: absolute;
    left: 300px;
    width: 600px;
    height: 343px;
    background: var(--paper);
    overflow: hidden;
    box-shadow: 0 6px 18px rgba(0,0,0,0.18);
  }
  .card--front { top: 50px; }
  .card--back { top: 477px; }

  .brand {
    position: absolute;
    left: 0; right: 0;
    display: flex;
    align-items: center;
    justify-content: center;
    gap: 12px;
    font-weight: 700;
    color: var(--ink);
  }
  .brand__dot {
    width: 14px; height: 14px;
    border-radius: 50%;
    background: var(--ink);
  }
  .card--front .brand { top: 82px; font-size: 22px; letter-spacing: 9px; }
  .card--back .brand { top: 128px; font-size: 40px; letter-spacing: 16px; }
  .card--back .brand__dot { width: 22px; height: 22px; }

  .rule {
    position: absolute;
    left: 0; right: 0;
    background: var(--ink);
  }
  .rule--upper { top: 150px; height: 5px; }
  .rule--lower { top: 283px; height: 5px; }
  .rule--base { top: 325px; height: 18px; }

  .name-plate {
    position: absolute;
    top: 138px;
    left: 188px;
    width: 224px;
    height: 34px;
    background: var(--ink);
    color: var(--paper);
    font-weight: 600;
    font-size: 18px;
    letter-spacing: 0.5px;
    display: flex;
    align-items: center;
    justify-content: center;
  }
  .job-title {
    position: absolute;
    top: 178px;
    left: 0; right: 0;
    text-align: center;
    font-size: 11px;
    font-weight: 400;
    letter-spacing: 0.8px;
  }
  .contact {
    position: absolute;
    display: flex;
    align-items: flex-start;
    gap: 12px;
    font-size: 11px;
    font-weight: 400;
    line-height: 1.35;
    color: var(--mute);
  }
  .contact svg { flex: none; margin-top: 1px; }
  .contact--phone { top: 190px; left: 56px; }
  .contact--address { top: 236px; left: 300px; }

  .tagline-band {
    position: absolute;
    left: 0; right: 0;
    top: 255px;
    height: 26px;
    background: var(--ink);
    color: var(--paper);
    font-size: 12.5px;
    font-weight: 300;
    letter-spacing: 1.2px;
    display: flex;
    align-items: center;
    justify-content: center;
    white-space: nowrap;
  }
</style>
</head>
<body>

  <section class="card card--front">
    <div class="brand"><span class="brand__dot"></span>HOPWELL</div>
    <div class="rule rule--upper"></div>
    <div class="name-plate">DELIA FENWICK</div>
    <div class="job-title">FOUNDER AND CPO</div>

    <div class="contact contact--phone">
      <svg width="14" height="14" viewBox="0 0 14 14" aria-hidden="true">
        <circle cx="7" cy="7" r="7" fill="var(--ink)"/>
        <path d="M4.6 3.8 L5.8 3.6 L6.3 5.2 L5.6 5.8 Q6.3 7.4 7.9 8.3 L8.6 7.6 L10.2 8.2 L10 9.4 Q9.6 10.2 8.6 10 Q4.6 9 4 5 Q3.9 4.1 4.6 3.8 Z" fill="var(--paper)"/>
      </svg>
      <span>720.555.0187</span>
    </div>

    <div class="contact contact--address">
      <svg width="14" height="14" viewBox="0 0 14 14" aria-hidden="true">
        <circle cx="7" cy="7" r="7" fill="var(--ink)"/>
        <path d="M7 3.2 A2.6 2.6 0 0 1 9.6 5.8 C9.6 7.6 7 10.6 7 10.6 C7 10.6 4.4 7.6 4.4 5.8 A2.6 2.6 0 0 1 7 3.2 Z" fill="var(--paper)"/>
        <circle cx="7" cy="5.8" r="0.9" fill="var(--ink)"/>
      </svg>
      <span>418 E. Harlow Avenue, Ste 2204,<br>Tampa, FL. 33719</span>
    </div>

    <div class="rule rule--lower"></div>
    <div class="rule rule--base"></div>
  </section>

  <section class="card card--back">
    <div class="brand"><span class="brand__dot"></span>HOPWELL</div>
    <div class="tagline-band">From the cooler to the dance floor...we bring the fun!</div>
  </section>

</body>
</html>
```